Orthodontist Needs Promotional Discount Postcard

5.5 x 8.5 Horizontal 2-Sided Postcard for mailing.
Images & Logo on both sides okay; must be free stock Images from legit sources only, or use attached images. See our website for information, CoveLineSmiles.com
Context to include:
New Patient Special $500 off Braces or Clear Aligners
Cannot be combined with any other discounts.
Major dental insurance plans and Vita-Plan accepted
Affordable payment options are available
Call to schedule your free consultation
Present this new patient offer to receive your discount.
Offer ends January 31, 2022.
805-419-2276 www. CoveLineSmiles.com
462 N. Marigold Street, Suite B, Ventura, CA 93001-5812
office@covelinesmiles.com

```html
<!DOCTYPE html>
<html lang="en">
<head>
<meta charset="utf-8">
<title>Cove Line Smiles – New Patient Postcard</title>
<link rel="stylesheet" href="https://fonts.googleapis.com/css2?family=Jost:wght@400;500&family=Ubuntu:wght@400;500;700&display=swap">
<style>
  :root {
    --brand-blue: #229fd9;
    --ink-gray: #58595b;
    --paper: #f4f4f4;
    --paper-cool: #eceef2;
    --backdrop: #a4a4a4;
    --white: #ffffff;
    --line-gray: #9a9a9a;
  }
  * { margin: 0; padding: 0; box-sizing: border-box; }
  html, body { width: 1066px; height: 1200px; overflow: hidden; }
  body { background: var(--backdrop); position: relative; font-family: "Jost", sans-serif; }

  .postcard {
    position: absolute; left: 174px; width: 730px; height: 472px;
    background: var(--paper); overflow: hidden;
    box-shadow: 0 10px 18px rgba(0,0,0,0.28);
  }
  .postcard--front { top: 98px; }
  .postcard--back { top: 623px; background: var(--paper-cool); }

  .brand { position: absolute; display: flex; align-items: center; gap: 10px; }
  .brand__dot { width: 80px; height: 80px; border-radius: 50%; background: var(--brand-blue); flex: none; }
  .brand__name {
    font-family: "Jost", sans-serif; font-weight: 500; color: var(--brand-blue);
    line-height: 1.02; letter-spacing: 1px; text-transform: uppercase;
  }
  .postcard--front .brand { left: 38px; top: 25px; }
  .postcard--front .brand__name { font-size: 31px; }

  .offer { position: absolute; left: 360px; width: 362px; top: 22px; text-align: center; }
  .offer__kicker { font-family: "Ubuntu", sans-serif; font-weight: 700; font-size: 27px; color: var(--ink-gray); line-height: 1; letter-spacing: 0.3px; }
  .offer__headline { font-family: "Ubuntu", sans-serif; font-weight: 700; color: var(--brand-blue); line-height: 1.02; margin-top: 2px; }
  .offer__headline span { display: block; }
  .offer__headline .big { font-size: 35px; }
  .offer__headline .mid { font-size: 31px; }
  .offer__terms { margin-top: 8px; font-size: 14px; color: var(--ink-gray); line-height: 17px; }

  .hero { position: absolute; left: 0; top: 0; }

  .contact-band {
    position: absolute; left: 0; bottom: 0; width: 100%; height: 38px;
    background: var(--brand-blue); color: var(--white);
    font-family: "Ubuntu", sans-serif; font-size: 20px; letter-spacing: 0.6px;
    display: flex; align-items: center; justify-content: center; gap: 10px;
  }

  .back-panel { position: absolute; left: 0; top: 0; width: 399px; height: 472px; }
  .back-copy { position: absolute; left: 33px; width: 332px; top: 302px; color: var(--white); }
  .back-copy__cta { font-family: "Ubuntu", sans-serif; font-weight: 700; font-size: 15px; letter-spacing: 0.1px; }
  .back-copy__note { font-family: "Ubuntu", sans-serif; font-size: 13px; margin-top: 2px; }
  .deadline {
    margin-top: 10px; height: 30px; background: var(--white); color: var(--brand-blue);
    font-family: "Ubuntu", sans-serif; font-weight: 500; font-size: 21px;
    display: flex; align-items: center; justify-content: center;
  }
  .back-copy__address { margin-top: 11px; font-size: 12.6px; }
  .back-copy__reach { font-size: 15px; margin-top: 1px; }
  .back-copy__web { font-weight: 500; font-size: 21px; letter-spacing: 0.2px; margin-top: 1px; }

  .postcard--back .brand { left: 433px; top: 14px; width: 160px; flex-direction: column; gap: 8px; }
  .postcard--back .brand__dot { width: 56px; height: 56px; }
  .postcard--back .brand__name { font-size: 22px; text-align: center; }

  .stamp-box { position: absolute; left: 623px; top: 27px; width: 80px; height: 84px; border: 1px solid #b8b8b8; }
  .address-block { position: absolute; left: 433px; top: 206px; width: 264px; }
  .address-block__label { font-family: "Ubuntu", sans-serif; font-weight: 500; font-size: 12px; color: #222; }
  .address-block__line { height: 1px; background: var(--line-gray); margin-top: 31px; }
  .address-block__line:first-of-type { margin-top: 9px; }
</style>
</head>
<body>

<section class="postcard postcard--front">
  <svg class="hero" width="730" height="472" viewBox="0 0 730 472">
    <defs>
      <linearGradient id="aligner-tones" x1="0" y1="0" x2="1" y2="0">
        <stop offset="0" stop-color="#eceef3"/>
        <stop offset="0.25" stop-color="#f2c9ae"/>
        <stop offset="0.6" stop-color="#eab192"/>
        <stop offset="1" stop-color="#e9a584"/>
      </linearGradient>
    </defs>
    <path role="img" aria-label="Close-up photo of a smile with a clear aligner being fitted"
          d="M0,250 C40,160 90,118 160,118 C260,118 340,160 430,190 C520,218 620,220 730,185 L730,434 L0,434 Z"
          fill="url(#aligner-tones)"/>
    <path d="M0,250 C40,160 90,118 160,118 C260,118 340,160 430,190 C520,218 620,220 730,185"
          fill="none" stroke="var(--brand-blue)" stroke-width="9"/>
  </svg>

  <div class="brand">
    <div class="brand__dot"></div>
    <div class="brand__name">Cove Line<br>Smiles</div>
  </div>

  <div class="offer">
    <p class="offer__kicker">NEW PATIENT SPECIAL</p>
    <h1 class="offer__headline">
      <span class="big">$500 OFF BRACES</span>
      <span class="mid">OR CLEAR ALIGNERS</span>
    </h1>
    <p class="offer__terms">Cannot be combined with any other discounts.<br>Major dental insurance plans &amp; Vita-Plan accepted<br>Affordable payment options are available</p>
  </div>

  <div class="contact-band">
    <span>CALL US : 805-419-2276</span><span>|</span><span>WWW.COVELINESMILES.COM</span>
  </div>
</section>

<section class="postcard postcard--back">
  <svg class="back-panel" width="399" height="472" viewBox="0 0 399 472">
    <defs>
      <linearGradient id="portrait-tones" x1="0" y1="0" x2="1" y2="0">
        <stop offset="0" stop-color="#6d7a4e"/>
        <stop offset="0.3" stop-color="#4a3126"/>
        <stop offset="0.55" stop-color="#d9a58e"/>
        <stop offset="0.8" stop-color="#3d2a22"/>
        <stop offset="1" stop-color="#5f7c48"/>
      </linearGradient>
    </defs>
    <rect x="0" y="0" width="399" height="472" fill="var(--brand-blue)"/>
    <path d="M0,220 C70,275 140,296 205,294 C290,292 360,262 399,217 L399,0 L0,0 Z" fill="var(--white)"/>
    <path role="img" aria-label="Photo of a smiling young woman outdoors"
          d="M0,207 C70,262 140,283 205,281 C290,279 360,250 399,204 L399,0 L0,0 Z"
          fill="url(#portrait-tones)"/>
  </svg>

  <div class="back-copy">
    <p class="back-copy__cta">CALL TO SCHEDULE YOUR FREE CONSULTATION</p>
    <p class="back-copy__note">Present this new patient offer to receive your discount.</p>
    <p class="deadline">OFFER ENDS JANUARY 31, 2022</p>
    <p class="back-copy__address">462 N. Marigold Street, Suite B, Ventura, CA 93001-5812</p>
    <p class="back-copy__reach">805-419-2276 | office@covelinesmiles.com</p>
    <p class="back-copy__web">WWW.COVELINESMILES.COM</p>
  </div>

  <div class="brand">
    <div class="brand__dot"></div>
    <div class="brand__name">Cove Line<br>Smiles</div>
  </div>

  <div class="stamp-box"></div>

  <div class="address-block">
    <p class="address-block__label">TO</p>
    <div class="address-block__line"></div>
    <div class="address-block__line"></div>
    <div class="address-block__line"></div>
    <div class="address-block__line"></div>
    <div class="address-block__line"></div>
  </div>
</section>

</body>
</html>
```